VENTURE CAPITAL GROUP BUSINESS CARD DESIGN

Venture Capital Group based in SF looking for a bold business card design. No trendy colour explosion, 3D effects etc. Just "simple" optical effects. Works on your brain, keeps your eye focused and sticks to your mind.
Target Market(s)
Technology startups
Industry/Entity Type
Venture Capital
Contact Information for Business Card
BARNABY WHITLOCK
MANAGING PARTNER
817 FERN ST SAN FRANCISCO, CA 94111
415.555.0143 O
415.555.0167 F
415.555.0192 C
barn@halcyonridgefund.example

```html
<!DOCTYPE html>
<html lang="en">
<head>
<meta charset="utf-8">
<title>Halcyon Ridge Capital Group — Business Card</title>
<link rel="stylesheet" href="https://fonts.googleapis.com/css2?family=Cinzel:wght@400;600&family=Cormorant+Garamond:wght@400;500&family=Montserrat:wght@300&display=swap">
<style>
  :root {
    --canvas-bg: #e9e7e3;
    --card-dark: #2b302e;
    --card-dark-edge: #1d211f;
    --card-light: #fbfbfb;
    --green: #1e9a3c;
    --green-bright: #3cc25a;
    --grey-text: #a9adab;
    --ink: #3a3d3c;
  }
  * { box-sizing: border-box; margin: 0; padding: 0; }
  html, body { width: 1200px; height: 1023px; overflow: hidden; }
  body {
    background: var(--canvas-bg);
    display: flex;
    flex-direction: column;
    align-items: center;
    justify-content: center;
    gap: 60px;
  }
  .card {
    width: 700px;
    height: 400px;
    border-radius: 6px;
    box-shadow: 0 10px 30px rgba(0,0,0,0.18);
    position: relative;
    overflow: hidden;
  }
  .card-front {
    background: radial-gradient(circle at 40% 35%, #3a403d 0%, var(--card-dark) 55%, var(--card-dark-edge) 100%);
    display: flex;
    flex-direction: column;
    align-items: center;
    justify-content: center;
  }
  .brand-name {
    font-family: "Cinzel", serif;
    font-weight: 400;
    font-size: 58px;
    letter-spacing: 2px;
    color: var(--green-bright);
    line-height: 1;
  }
  .brand-tagline {
    font-family: "Montserrat", sans-serif;
    font-weight: 300;
    font-size: 17px;
    letter-spacing: 9px;
    color: var(--grey-text);
    margin-top: 14px;
  }
  .card-back {
    background: var(--card-light);
    display: flex;
    align-items: center;
    padding: 0 56px;
  }
  .contact-block { flex: 1; }
  .person-name {
    font-family: "Cinzel", serif;
    font-weight: 600;
    font-size: 24px;
    color: var(--ink);
    letter-spacing: 1px;
  }
  .person-title {
    font-family: "Montserrat", sans-serif;
    font-weight: 300;
    font-size: 12px;
    letter-spacing: 4px;
    color: var(--green);
    margin: 6px 0 26px;
  }
  .contact-list { list-style: none; }
  .contact-item {
    display: flex;
    align-items: center;
    gap: 12px;
    margin-bottom: 10px;
    font-family: "Cormorant Garamond", serif;
    font-weight: 500;
    font-size: 18px;
    color: var(--green);
  }
  .contact-icon { width: 22px; height: 22px; flex: none; }
  .back-brand {
    font-family: "Cinzel", serif;
    font-weight: 400;
    font-size: 30px;
    color: var(--green);
    text-align: right;
    line-height: 1.15;
  }
</style>
</head>
<body>
  <section class="card card-front">
    <div class="brand-name">HALCYON RIDGE</div>
    <div class="brand-tagline">CAPITAL GROUP</div>
  </section>

  <section class="card card-back">
    <div class="contact-block">
      <div class="person-name">BARNABY WHITLOCK</div>
      <div class="person-title">MANAGING PARTNER</div>
      <ul class="contact-list">
        <li class="contact-item">
          <svg class="contact-icon" viewBox="0 0 22 22"><circle cx="11" cy="11" r="11" fill="#1e9a3c"/><path d="M11 5a4 4 0 0 0-4 4c0 3 4 8 4 8s4-5 4-8a4 4 0 0 0-4-4z" fill="#fff"/><circle cx="11" cy="9" r="1.5" fill="#1e9a3c"/></svg>
          817 FERN ST SAN FRANCISCO, CA 94111
        </li>
        <li class="contact-item">
          <svg class="contact-icon" viewBox="0 0 22 22"><circle cx="11" cy="11" r="11" fill="#1e9a3c"/><path d="M7 6h3l1 3-2 1a7 7 0 0 0 3 3l1-2 3 1v3a1 1 0 0 1-1 1A10 10 0 0 1 6 7a1 1 0 0 1 1-1z" fill="#fff"/></svg>
          415.555.0143 O
        </li>
        <li class="contact-item">
          <svg class="contact-icon" viewBox="0 0 22 22"><circle cx="11" cy="11" r="11" fill="#1e9a3c"/><rect x="6" y="9" width="10" height="7" rx="1" fill="#fff"/><rect x="8" y="5" width="6" height="4" fill="#fff"/></svg>
          415.555.0167 F
        </li>
        <li class="contact-item">
          <svg class="contact-icon" viewBox="0 0 22 22"><circle cx="11" cy="11" r="11" fill="#1e9a3c"/><rect x="8" y="5" width="6" height="12" rx="1" fill="#fff"/><circle cx="11" cy="15" r="0.8" fill="#1e9a3c"/></svg>
          415.555.0192 C
        </li>
        <li class="contact-item">
          <svg class="contact-icon" viewBox="0 0 22 22"><circle cx="11" cy="11" r="11" fill="#1e9a3c"/><rect x="5.5" y="7" width="11" height="8" rx="1" fill="#fff"/><path d="M5.5 7.5l5.5 4 5.5-4" stroke="#1e9a3c" stroke-width="1" fill="none"/></svg>
          barn@halcyonridgefund.example
        </li>
      </ul>
    </div>
    <div class="back-brand">HALCYON<br>RIDGE</div>
  </section>
</body>
</html>
```